Brochure required

Looking at getting business brochure designed for my solar sales company. i will require a range of products to be listed on the brochure I require a simple/ elegent / professional looking brochure.

I am happy to provide designer with all the required information that must go into the brochure. otherwise please visit www.velkariston.com.au and view the products which i would like to allocate into the brochure aswell as our company logo and a little about me section

```html
<!DOCTYPE html>
<html lang="en">
<head>
<meta charset="utf-8">
<title>Velkariston – Energy Solutions Brochure</title>
<link href="https://fonts.googleapis.com/css2?family=Montserrat:wght@300;400;600;700;800&display=swap" rel="stylesheet">
<style>
  :root{
    --blue:#1a6ea6;
    --sky:#37a9d3;
    --yellow:#dcc427;
    --teal:#2fc79b;
    --ink:#2b2f3a;
    --grey:#4a4d55;
    --paper:#f2f2f2;
    --page:#fafafa;
    --stage:#e9e9e9;
  }
  *{margin:0;padding:0;box-sizing:border-box}
  html,body{width:1200px;height:840px;overflow:hidden}
  body{background:var(--stage);font-family:'Montserrat',sans-serif;color:var(--ink);position:relative}
  .spread{position:absolute;left:40px;top:80px;width:1120px;height:680px;display:flex;box-shadow:0 10px 30px rgba(0,0,0,.12)}
  .page{position:relative;width:560px;height:680px;overflow:hidden}
  .page--back{background:var(--paper)}
  .page--front{background:var(--page)}
  .page svg.shapes{position:absolute;inset:0;width:100%;height:100%}
  .abs{position:absolute}

  /* back cover */
  .cover-title{left:40px;top:40px;line-height:1}
  .cover-title .energy{font-size:74px;font-weight:800;color:var(--blue);font-style:italic;letter-spacing:1px}
  .cover-title .solutions{font-size:50px;font-weight:400;color:var(--grey);letter-spacing:1px;margin-top:4px}
  .cover-title .tagline{font-size:20px;font-weight:300;color:var(--grey);letter-spacing:1px;margin-top:6px}
  .contact{left:0;width:560px;top:585px;text-align:center}
  .contact h3{font-size:17px;font-weight:400;color:var(--blue);letter-spacing:1px}
  .contact p{font-size:11px;color:var(--grey);margin-top:8px;display:flex;justify-content:center;align-items:center;gap:8px}
  .contact svg{width:12px;height:12px}

  /* front cover */
  .brand{right:30px;top:70px;display:flex;align-items:center;gap:8px}
  .brand .mark{width:22px;height:22px;background:var(--teal)}
  .brand .name{font-size:30px;font-weight:700;color:var(--ink)}
  .front-title{left:50px;top:150px}
  .front-title .row{display:flex;align-items:flex-end;gap:12px}
  .front-title .energy{background:var(--ink);color:var(--yellow);font-size:36px;font-weight:800;padding:2px 10px;line-height:1.1}
  .front-title .solutions{color:#fff;font-size:34px;font-weight:800;line-height:1}
  .front-title .tagline{font-size:14px;font-weight:600;color:var(--ink);margin-top:6px;letter-spacing:.5px}

  .pride{left:30px;top:478px}
  .pride h2{font-size:26px;font-weight:800;color:var(--blue);letter-spacing:.5px;line-height:1.1}
  .pride .sub{font-size:12px;color:var(--sky);font-weight:600;margin-top:3px}
  .services{display:flex;flex-direction:column;gap:5px}
  .services--left{left:30px;top:530px;width:245px}
  .services--right{left:292px;top:534px;width:245px}
  .service h4{font-size:11px;font-weight:700;color:var(--sky);letter-spacing:.3px;line-height:1.25}
  .service p{font-size:8.3px;line-height:1.32;color:var(--grey);margin-top:2px;text-align:justify}
  .footer-url{right:26px;bottom:12px;color:#fff;font-size:13px;font-weight:600}
</style>
</head>
<body>
<div class="spread">

  <!-- BACK COVER -->
  <section class="page page--back">
    <svg class="shapes" viewBox="0 0 560 680">
      <polygon points="420,60 560,60 560,160 445,150" fill="var(--blue)"/>
      <polygon points="0,285 300,285 360,228 560,228 560,560 230,560 0,560" fill="var(--yellow)"/>
      <polygon points="0,640 95,640 70,680 0,680" fill="var(--blue)"/>
      <polygon points="110,648 470,648 450,680 95,680" fill="var(--yellow)"/>
      <polygon points="470,648 560,648 560,680 450,680" fill="var(--blue)"/>
    </svg>
    <svg class="shapes" viewBox="0 0 560 680">
      <defs>
        <linearGradient id="gA" x1="0" y1="0" x2="0" y2="1"><stop offset="0" stop-color="#9fb2c2"/><stop offset="1" stop-color="#1d2740"/></linearGradient>
        <linearGradient id="gB" x1="0" y1="0" x2="0" y2="1"><stop offset="0" stop-color="#a9c6de"/><stop offset="1" stop-color="#6d4a3a"/></linearGradient>
        <linearGradient id="gC" x1="0" y1="0" x2="0" y2="1"><stop offset="0" stop-color="#5e90c4"/><stop offset="1" stop-color="#9cc6e8"/></linearGradient>
      </defs>
      <polygon role="img" aria-label="Photo: installers carrying solar panels on a rooftop" points="12,298 345,298 262,380 262,548 12,548" fill="url(#gA)"/>
      <polygon role="img" aria-label="Photo: workers fitting a solar panel on a tiled roof" points="372,240 548,240 548,372 290,372" fill="url(#gB)"/>
      <polygon role="img" aria-label="Photo: small solar panel on a pole against a fence" points="300,386 548,386 548,548 330,548 276,492 276,410" fill="url(#gC)"/>
    </svg>

    <div class="abs cover-title">
      <div class="energy">ENERGY</div>
      <div class="solutions">SOLUTIONS</div>
      <div class="tagline">For A CHANGING WORLD</div>
    </div>

    <div class="abs contact">
      <h3>CONTACT US</h3>
      <p>
        <svg viewBox="0 0 12 12"><circle cx="6" cy="6" r="6" fill="var(--blue)"/><circle cx="6" cy="6" r="3.5" fill="none" stroke="#fff" stroke-width="1"/></svg>
        www.velkariston.com.au &nbsp;|&nbsp;
        <svg viewBox="0 0 12 12"><circle cx="6" cy="6" r="6" fill="var(--blue)"/><path d="M4 3.2l1.2 1.4-.6.8a4 4 0 0 0 2 2l.8-.6 1.4 1.2-.8 1A5 5 0 0 1 3 4z" fill="#fff"/></svg>
        0412 555 019
      </p>
    </div>
  </section>

  <!-- FRONT COVER -->
  <section class="page page--front">
    <svg class="shapes" viewBox="0 0 560 680">
      <defs>
        <linearGradient id="gP" x1="0" y1="0" x2="1" y2="1"><stop offset="0" stop-color="#3c5f95"/><stop offset=".6" stop-color="#1b2a55"/><stop offset="1" stop-color="#b7bcc4"/></linearGradient>
      </defs>
      <polygon points="0,60 110,60 150,200 0,200" fill="var(--sky)"/>
      <polygon points="120,60 145,60 190,200 165,200" fill="var(--yellow)"/>
      <polygon role="img" aria-label="Photo: rows of blue solar panels in sunlight" points="0,200 560,200 560,465 520,465 505,500 0,455" fill="url(#gP)"/>
      <polygon points="310,330 560,330 560,385 335,385" fill="var(--teal)"/>
      <polygon points="30,120 430,120 480,235 440,345 30,300" fill="var(--yellow)"/>
      <polygon points="380,504 455,504 468,526 393,526" fill="var(--yellow)"/>
      <polygon points="465,504 560,504 560,527 476,527" fill="var(--blue)"/>
      <polygon points="0,652 40,652 58,680 0,680" fill="var(--blue)"/>
      <polygon points="55,652 560,636 560,680 75,680" fill="var(--yellow)"/>
    </svg>

    <div class="abs brand">
      <span class="mark"></span>
      <span class="name">Velkariston</span>
    </div>

    <div class="abs front-title">
      <div class="row">
        <span class="energy">ENERGY</span>
        <span class="solutions">SOLUTIONS</span>
      </div>
      <div class="tagline">FOR A CHANGING WORLD.</div>
    </div>

    <div class="abs pride">
      <h2>WE PRIDE OURSELVES</h2>
      <div class="sub">On providing premium quality solar services</div>
    </div>

    <div class="abs services services--left">
      <div class="service">
        <h4>SYSTEM MAINTENANC &amp; CLEANING</h4>
        <p>Just like running a car, regular servicing is the best way to ensure your solar panel system keeps operating safely, correctly and efficiently.</p>
      </div>
      <div class="service">
        <h4>SOLAR INSTALLATION AUDITING</h4>
        <p>Installers are required to provide systems that meet Australian standards and only around 8% were able to meet them with only minor deviations. Just 2.5% were rated as "industry best practice".</p>
      </div>
    </div>

    <div class="abs services services--right">
      <div class="service">
        <h4>MAINTENANCE SCHEDULES</h4>
        <p>It is important that regular maintenance is carried out on your solar panel system so it keeps operating safely and efficiently.</p>
      </div>
      <div class="service">
        <h4>SOLAR SYSTEM MONITORING</h4>
        <p>Solar power is a fantastic long-term investment that can cut your greenhouse emissions and bills.</p>
      </div>
    </div>

    <div class="abs footer-url">www.velkariston.com.au</div>
  </section>

</div>
</body>
</html>
```